Business Card Design

Provide project management services to the construction and other industries
Construction services - Civil and Concrete works
Shop Detailing
Structural Modelling
Client side coordination of project teams and consultants
Feasibility Studies for construction projects

Industry/Entity Type

Business

Contact Information for Business Card

Plan Sure
Derek Calloway B.Sc (Civil), M.Proj.Mgt.
Director

m: 0412 738 564
e: dcalloway@plansure.com.au

p: 08 6358 2714
a: 17 Banksia Court, Ashdale, WA 6180

```html
<!DOCTYPE html>
<html lang="en">
<head>
<meta charset="utf-8">
<title>Plan Sure — Business Card</title>
<link rel="stylesheet" href="https://fonts.googleapis.com/css2?family=Source+Sans+3:wght@400;600;700;800&display=swap">
<style>
  :root {
    --brand-green: #3a780b;
    --ink: #1f1f1f;
    --paper: #ffffff;
    --backdrop: #ecebe7;
    --rule: #232323;
  }
  * { margin: 0; padding: 0; box-sizing: border-box; }
  html, body { width: 1200px; height: 900px; overflow: hidden; }
  body {
    background: var(--backdrop);
    font-family: "Source Sans 3", Arial, sans-serif;
    position: relative;
  }
  .card {
    position: absolute;
    top: 285px;
    width: 520px;
    height: 318px;
    border-radius: 3px;
    overflow: hidden;
    box-shadow: 0 8px 22px rgba(0,0,0,0.18);
  }
  .card--back { left: 55px; background: var(--brand-green); display: flex; align-items: center; justify-content: center; }
  .card--front { left: 625px; background: var(--paper); }

  .wordmark {
    font-weight: 800;
    font-size: 50px;
    letter-spacing: 3px;
    text-transform: uppercase;
    line-height: 1;
    white-space: nowrap;
  }
  .card--back .wordmark { color: var(--paper); }

  .front__head {
    height: 140px;
    display: flex;
    align-items: center;
    justify-content: center;
  }
  .front__head .wordmark { color: var(--ink); }
  .front__rule { height: 6px; background: var(--rule); }
  .front__gap { height: 5px; background: var(--paper); }
  .front__body {
    position: absolute;
    left: 0; right: 0; top: 151px; bottom: 0;
    background: var(--brand-green);
    color: var(--paper);
  }
  .person { position: absolute; left: 30px; top: 24px; }
  .person__name { font-size: 21px; font-weight: 700; line-height: 1.1; white-space: nowrap; }
  .person__creds { font-size: 13px; font-weight: 600; margin-left: 3px; }
  .person__role { font-size: 15px; margin-top: 4px; }
  .person__address { font-size: 15px; line-height: 1.45; margin-top: 16px; font-style: normal; }

  .contact {
    position: absolute; right: 24px; top: 16px;
    list-style: none; text-align: right; font-size: 13px; line-height: 1;
  }
  .contact li { display: flex; align-items: center; justify-content: flex-end; gap: 6px; margin-bottom: 8px; white-space: nowrap; }
  .contact li.contact__email { margin-top: 16px; }
  .contact svg { width: 11px; height: 11px; flex: none; }
</style>
</head>
<body>
  <section class="card card--back" aria-label="Card back">
    <span class="wordmark">Plan Sure</span>
  </section>

  <section class="card card--front" aria-label="Card front">
    <div class="front__head"><span class="wordmark">Plan Sure</span></div>
    <div class="front__rule"></div>
    <div class="front__gap"></div>
    <div class="front__body">
      <div class="person">
        <p class="person__name">Derek Calloway<span class="person__creds">B.Sc (Civil), M.Proj.Mgt.</span></p>
        <p class="person__role">Director</p>
        <address class="person__address">17 Banksia Court,<br>Ashdale, WA 6180</address>
      </div>
      <ul class="contact">
        <li>08 6358 2714
          <svg viewBox="0 0 12 12" aria-hidden="true"><path fill="#fff" d="M2.5 1h2l1 2.6-1.3 1a6 6 0 0 0 3.2 3.2l1-1.3L11 7.5v2A1.5 1.5 0 0 1 9.5 11C5 11 1 7 1 2.5A1.5 1.5 0 0 1 2.5 1z"/></svg>
        </li>
        <li>0412 738 564
          <svg viewBox="0 0 12 12" aria-hidden="true"><rect x="3" y="0.8" width="6" height="10.4" rx="1" fill="none" stroke="#fff" stroke-width="1.2"/><circle cx="6" cy="9.3" r="0.7" fill="#fff"/></svg>
        </li>
        <li class="contact__email">dcalloway@plansure.com.au
          <svg viewBox="0 0 12 12" aria-hidden="true"><rect x="0.5" y="2" width="11" height="8" fill="#fff"/><path d="M1 2.5l5 4 5-4" fill="none" stroke="#3a780b" stroke-width="1"/></svg>
        </li>
      </ul>
    </div>
  </section>
</body>
</html>
```